Social News web page design website name Velnu.

I need a web design for a start up project called Velnu based in Sydney. Its a social news website. it helps people to get centralized news and people can have their own profiles where they can post there thoughts and comments and it will be free to signup and usage as well.

I would like to see designs that use the latest murlan bootstrap framework and are mobile compatible. only need 2 pages a home page kind of similar to
plom (http://plom.example/) and a profile that's a next gen user profile page I will leave that to you imaginations

this is my previous design I did on my own http://www.velnu-site.example/

Target Market(s)

target market is 13 and up and anyone who likes or uses social media and would be able to understand the site

Industry/Entity Type

News

Requirements
Must have
• 1.) using murlan bootstrap. 2) a home page similar to plom (http://plom.example/) or even better free to use your imagination 3) a next gen profile page better the one i made on my own which is this one (http://www.velnu-site.example/profile/korelatimbo) 4) for mobile navigation, have a mobile navigation something similar to http://zanpel.wovrite.example/
Nice to have
• 1) a sexy navigation and layout for both desktop and mobile phones. i will leave that to you imaginations. 2) social medial buttons like to sign-in with and also to post a story to Linkora or murlan 3) a user settings page (but not necessary) 4) a login or signup (but not necessary)

```html
<!DOCTYPE html>
<html lang="en">
<head>
<meta charset="utf-8">
<title>Velnu — Social News</title>
<link href="https://fonts.googleapis.com/css2?family=Open+Sans:wght@400;600;700&family=Arimo:wght@400;700&display=swap" rel="stylesheet">
<style>
:root{
  --ink:#222;
  --text:#555;
  --muted:#333;
  --link:#2a9fd6;
  --source:#3b8fb8;
  --yellow:#ffe000;
  --topbar:#1c1c1c;
  --footer:#2b2b2b;
  --band:#e9e8e9;
  --teal:#19b394;
  --social:#3a9fbf;
}
*{box-sizing:border-box;margin:0;padding:0}
html,body{width:964px;height:1200px;overflow:hidden;background:#fff}
body{position:relative;font-family:"Arimo",Arial,sans-serif;color:var(--text)}
.abs{position:absolute}

.topbar{left:0;top:0;width:964px;height:24px;background:var(--topbar)}
.topbar .social{position:absolute;left:702px;top:0;height:20px;width:118px;background:#141414;display:flex;gap:12px;align-items:center;justify-content:center}
.social i{display:block;width:10px;height:10px;background:var(--social);border-radius:2px}

.header{left:0;top:24px;width:964px;height:52px;border-bottom:1px solid #e6d200}
.logo{position:absolute;left:155px;top:11px;font-family:"Open Sans",sans-serif;font-weight:700;font-size:24px;color:var(--ink)}
.nav{position:absolute;left:528px;top:19px;display:flex;gap:14px;font-size:13px;color:var(--muted)}
.nav span.sep{color:#777}
.signin{position:absolute;left:748px;top:17px;font-size:14px;color:var(--link)}
.search-icon{position:absolute;left:808px;top:18px}

.hero{left:0;top:77px;width:964px;height:279px;background:var(--yellow)}
.hero .device{position:absolute;left:65px;top:19px;width:408px;height:237px;border-radius:8px 8px 4px 4px;background:linear-gradient(135deg,#1f2a33 0%,#8fb4c9 40%,#dbe9f1 60%,#2c3a44 100%)}
.hero .arrow{position:absolute;top:108px}
.hero-copy{position:absolute;right:60px;top:48px;width:420px;text-align:right;color:var(--ink)}
.hero-copy h1{font-family:"Open Sans",sans-serif;font-weight:400;font-size:36px;line-height:42px;letter-spacing:.5px}
.hero-copy h2{font-family:"Open Sans",sans-serif;font-weight:400;font-size:14.5px;line-height:15px;margin-top:8px;text-transform:uppercase;color:#333}
.hero-copy p{font-size:8.6px;line-height:10.5px;margin-top:7px;color:#333}

.pager{display:flex;gap:2px}
.pager b{width:14px;height:14px;display:flex;align-items:center;justify-content:center;font-size:9px;font-weight:700}
.pager .prev{background:var(--yellow);color:#333}
.pager .next{background:#111;color:#fff}

.featured{left:0;top:356px;width:964px;height:358px}
.featured .pager{position:absolute;left:794px;top:16px}
.story{position:absolute;top:38px;width:217px}
.story .photo{height:134px}
.story h3{margin-top:8px;font-size:14px;line-height:17px;font-weight:700;color:var(--ink);text-align:justify;text-align-last:left}
.story .source{margin-top:3px;font-size:12px;font-weight:700;color:var(--source)}
.story .summary{margin-top:4px;font-size:11.4px;line-height:13.2px;color:#666;text-align:justify;height:52px;overflow:hidden}
.story .more{margin:6px 0 0 4px;font-size:12px;color:var(--link)}
.story .actions{display:flex;align-items:center;gap:16px;margin:1px 0 0 3px}
.btn-share{background:var(--teal);color:#fff;font-size:10px;padding:0 7px;height:23px;line-height:23px;border-radius:2px}
.vote{font-size:10px;color:#666}

.trends{left:0;top:714px;width:964px;height:180px;background:var(--band)}
.section-title{position:absolute;font-family:"Open Sans",sans-serif;font-weight:600;font-size:17.5px;color:#555}
.view-all{background:#111;color:#fff;font-size:7.5px;font-weight:700;padding:0 10px;height:13px;line-height:13px}
.tools{position:absolute;display:flex;gap:6px;align-items:center}
.tile{position:absolute;width:160px}
.tile .photo{height:88px}
.tile h4{margin-top:6px;font-family:"Open Sans",sans-serif;font-weight:700;font-size:10.3px;color:var(--ink);white-space:nowrap}
.tile .meta{margin-top:8px;font-size:9.6px;color:#444}
.tile .date{margin-top:6px;font-size:9.6px;color:#444}

.popular{left:0;top:894px;width:964px;height:236px}

.footer{left:0;top:1130px;width:964px;height:70px;background:var(--footer)}
.footer .legal{position:absolute;left:142px;top:27px;font-size:10px;color:#fff}
.footer .social{position:absolute;left:552px;top:30px;display:flex;gap:13px}
.footer .social i{background:#666;width:9px;height:9px}
.footer .search{position:absolute;left:662px;top:22px;width:158px;height:19px;background:#3a3a3a;color:#666;font-size:8px;text-align:right;padding:5px 5px 0 0}
</style>
</head>
<body>

<div class="abs topbar">
  <div class="social"><i></i><i></i><i></i><i></i><i></i></div>
</div>

<header class="abs header">
  <div class="logo">Velnu</div>
  <nav class="nav"><span>HOME</span><span class="sep">:</span><span>VIDEO</span><span class="sep">:</span><span>READER</span></nav>
  <div class="signin">Sign in</div>
  <svg class="search-icon" width="14" height="14" viewBox="0 0 14 14"><circle cx="5.5" cy="5.5" r="4" fill="none" stroke="#666" stroke-width="2"/><line x1="8.5" y1="8.5" x2="13" y2="13" stroke="#666" stroke-width="2.4"/></svg>
</header>

<section class="abs hero">
  <svg class="arrow" style="left:66px" width="14" height="20" viewBox="0 0 14 20"><polyline points="11,2 3,10 11,18" fill="none" stroke="#111" stroke-width="3"/></svg>
  <div class="device" role="img" aria-label="Laptop showing a glass office tower"></div>
  <svg class="arrow" style="left:458px" width="14" height="20" viewBox="0 0 14 20"><polyline points="3,2 11,10 3,18" fill="none" stroke="#111" stroke-width="3"/></svg>
  <div class="hero-copy">
    <h1>VESTIBULUM GET!</h1>
    <h2>Lorem ipsum dolor sit amet, acosectetur vestibulum egestas mauris mas</h2>
    <p>Ut pulvinar mi diam. Suspendisse non arcu sem. Aenean eu posuere eros. Cras ahendrerit felis at laoreet tristique, eros eros posuere dolor, ac lacinia orci tortort erat!</p>
    <p>Donec vel nibh est. Cras eu magna ligula, ut congue nunc. Nulla vestibulum fermentum tconvallis. Praesent feugiat mauris non tortor bibendum non aliquet lectus lobortis donec id commodo purus. Phasellus nisi nisl, fringilla ut adipiscing vel!</p>
    <p>Dictum et sapien!</p>
  </div>
</section>

<section class="abs featured">
  <div class="pager"><b class="prev">&lsaquo;</b><b class="next">&rsaquo;</b></div>

  <article class="story" style="left:140px">
    <div class="photo" role="img" aria-label="Injured football linebacker sitting on the field" style="background:linear-gradient(135deg,#2b4a7a,#c9c2b8 50%,#3d5f92)"></div>
    <h3>Darvell Ostrin Injury: Updates on Harbor Kings LB's Leg and Return</h3>
    <div class="source">benchline.example</div>
    <p class="summary">Bayport Harbor Kings linebacker Darvell Ostrin suffered a scary injury in the NCL Championship Game against the Northshore Gales</p>
    <div class="more">View summary</div>
    <div class="actions"><span class="btn-share">&#8599; Share Story &#9662;</span><span class="vote">Vote ( &#9757;0 )</span></div>
  </article>

  <article class="story" style="left:375px">
    <div class="photo" role="img" aria-label="Portrait of an elderly film director" style="background:linear-gradient(135deg,#e8e4df,#c9a58e 55%,#efeae6)"></div>
    <h3>Film: Silver Lanterns: Ehrenpreis für Walden Aster</h3>
    <div class="source">www.blickpunkt.example</div>
    <p class="summary">Aster hat über 55 Filme gedreht, zuletzt war „Blaue Lilie" mit Arlo Brenner und Cora Blanford in den Kinos. Trotz dutzender Nominierungen hat der vierfache Orion- und</p>
    <div class="more">View summary</div>
    <div class="actions"><span class="btn-share">&#8599; Share Story &#9662;</span><span class="vote">Vote ( &#9757;0 )</span></div>
  </article>

  <article class="story" style="left:609px">
    <div class="photo" role="img" aria-label="Alien city skyline with a spaceship" style="background:linear-gradient(160deg,#6b6e73,#3a3d42 55%,#1e2024)"></div>
    <h3>Some of the Most Plausible Scenarios for Alien Civilizations</h3>
    <div class="source">futurescan.example</div>
    <p class="summary">We have yet to make contact with an extraterrestrial intelligence, making it exceedingly difficult for us to imagine what an alien civilization mig...</p>
    <div class="more">View summary</div>
    <div class="actions"><span class="btn-share">&#8599; Share Story &#9662;</span><span class="vote">Vote ( &#9757;0 )</span></div>
  </article>
</section>

<section class="abs trends">
  <h2 class="section-title" style="left:143px;top:6px">INTERNET TRENDS</h2>
  <div class="tools" style="left:733px;top:20px"><span class="view-all">VIEW ALL</span><div class="pager"><b class="prev">&lsaquo;</b><b class="next">&rsaquo;</b></div></div>

  <div class="tile" style="left:142px;top:32px">
    <div class="photo" role="img" aria-label="Hockey players and referees on the ice" style="background:linear-gradient(135deg,#2d3f5e,#b9bcc4 50%,#1f2e4a)"></div>
    <h4>Coastline Otters coach Joh....</h4><div class="meta">Canada &nbsp;a day ago</div>
  </div>
  <div class="tile" style="left:316px;top:32px">
    <div class="photo" role="img" aria-label="Two quarterbacks meeting after a game" style="background:linear-gradient(135deg,#1d2a3a,#8a8f96 50%,#e3e3e3)"></div>
    <h4>Grand Bowl 2014: Mesa Bro...</h4><div class="meta">Canada &nbsp;a day ago</div>
  </div>
  <div class="tile" style="left:490px;top:32px">
    <div class="photo" role="img" aria-label="Television broadcast set inside a stadium" style="background:linear-gradient(180deg,#9aa0aa,#b3323a 45%,#2a2a36)"></div>
    <h4>All four NPL network partne...</h4><div class="meta">Australia &nbsp;a day ago</div>
  </div>
  <div class="tile" style="left:664px;top:32px">
    <div class="photo" role="img" aria-label="Celebrities reacting at an awards ceremony" style="background:linear-gradient(135deg,#b98a74,#4a3a34 50%,#c27c6e)"></div>
    <h4>SPG Awards 2014:</h4><div class="meta">United Kingdom a day ago</div>
  </div>
</section>

<section class="abs popular">
  <h2 class="section-title" style="left:140px;top:17px">POPULAR STORIES</h2>
  <div class="tools" style="left:731px;top:27px"><span class="view-all">VIEW ALL</span><div class="pager"><b class="prev">&lsaquo;</b><b class="next">&rsaquo;</b></div></div>

  <div class="tile" style="left:139px;top:46px">
    <div class="photo" role="img" aria-label="Portrait of a smiling man indoors" style="background:linear-gradient(135deg,#a08a6c,#4a3a2e 50%,#c2ae92)"></div>
    <h4>The most basic question is</h4><div class="meta" style="margin-top:6px">Australia</div><div class="date">23 Sep, 2013</div>
  </div>
  <div class="tile" style="left:313px;top:46px">
    <div class="photo" role="img" aria-label="Portrait of a bearded man in a suit" style="background:linear-gradient(135deg,#3a2d26,#b08e76 50%,#2a2424)"></div>
    <h4>The two most important days...</h4><div class="meta" style="margin-top:6px">Australia</div><div class="date">23 Sep, 2013</div>
  </div>
  <div class="tile" style="left:487px;top:46px">
    <div class="photo" role="img" aria-label="Portrait of a young man in a suit" style="background:linear-gradient(180deg,#d8d8d8,#d9b394 55%,#2a2a2a)"></div>
    <h4>In the practice of toleranc...</h4><div class="meta" style="margin-top:6px">Australia</div><div class="date">23 Sep, 2013</div>
  </div>
  <div class="tile" style="left:661px;top:46px">
    <div class="photo" role="img" aria-label="Close-up portrait of a man" style="background:linear-gradient(135deg,#2f5f9e,#c59c82 50%,#bfcbd6)"></div>
    <h4>The two most important days...</h4><div class="meta" style="margin-top:6px">Australia</div><div class="date">23 Sep, 2013</div>
  </div>
</section>

<footer class="abs footer">
  <div class="legal">VELNU© 2014 &nbsp;| &nbsp;PRIVACY POLICY</div>
  <div class="social"><i></i><i></i><i></i><i></i><i></i></div>
  <div class="search">Search the Site</div>
</footer>

</body>
</html>
```